qLM Builders
Nimble Site Crafting
draft #229 - This looks pretty good. We prefer option 2 for the stationary. Clean and simple. We aren't so sure about the colored watermark. Seems like too much maybe
draft #223 - We really like the back of this one!
The contests has been extended for 3 more days. Please submit new designs. Due to the short time frame, we will only be accepting and rating full designs including complete stationary.
I will make every effort to provide feedback as soon as possible on designs concepts. Thank!
draft #96 - I like the back! The front is a little cookie cutter. Can you try something that integrates the "X" into the design. I don't really like the text all centered (draft #95,draft #94)
draft #102 I don't like the graphic at the top, but I like the back and I like how you integrated the X on the front like a watermark. can you remove that and add some icon's for phone,email, ect?
Some design inspiration - here are some cards we like
http://www.cardmarket.example/theme_previews/1778907-stylish-business-card?index=4
http://cardmarket.example/item/royal-modern-business-card/2484567?WT.ac=category_thumb&WT.seg_1=category_thumb&WT.z_author=omar-lindqvest
http://cardmarket.example/item/awesomeness-business-card/55256?WT.ac=category_thumb&WT.seg_1=category_thumb&WT.z_author=Bram
http://cardmarket.example/item/qr-business-card/1361513?WT.ac=category_thumb&WT.seg_1=category_thumb&WT.z_author=Marisk
http://cardmarket.example/item/clean-modern-business-card/1922436?WT.ac=category_thumb&WT.seg_1=category_thumb&WT.z_author=dustwick
http://cardmarket.example/theme_previews/1492534-neat-corporate-business-card?index=9
http://cardmarket.example/item/red-business-card/504464?WT.ac=category_thumb&WT.seg_1=category_thumb&WT.z_author=lumenpress
Also meant to mention, we prefer square cards (instead of the rounded corners).
If you have ideas for texture/embossing that would look nice please include! We are digging the glossy look on the back of some of these. But any details that help make the card unique is great!
thanks again!
Hi Designers. We got backed up and haven't been able to provide feedback yet.
There are also A LOT of designs to go through. We will be eliminating design's I consider "cookie cutter" templates. We are interested in unique designs that integrate the with the look and feel of the logo, or directly integrate parts of the logo with the designs.
In General, the Wavy/curvy look isn't what we are going for (there are A LOT of those).
There are some very unique integrations with the "X" that we like, especially when it's used kinda like a watermark.
We don't want any contact info on the back other then maybe the website.
Again thanks for your work! We will be sending specific feedback for the designs we like via PM in the next few hours.
Gavin@qlmbuilders
Thanks for all the designs and the note. We will be going through and selecting the few our favorite designs so far and offering tomorrow.
Thanks for the good work!
@PH - we will develop stationery for the liked business cards. Please let me know via private message. Thanks
sir please check pvt message top right side please
Note to Designers - This a a business Card & Stationary project. Designs should include concepts for both. Any questions or concerns please message me.

```html
<!DOCTYPE html>
<html lang="en">
<head>
<meta charset="utf-8">
<title>qLM Builders – Business Card</title>
<link rel="stylesheet" href="https://fonts.googleapis.com/css2?family=Open+Sans:wght@400;600;700&display=swap">
<style>
  :root {
    --bg: #2a2a2a;
    --card: #ffffff;
    --card-shade: #e2e2e2;
    --brand-blue: #2aa6d9;
    --ink: #3a3a3a;
    --ink-soft: #6a6a6a;
    --mark-dark: #141414;
    --mark-mid: #8a8a8a;
  }
  * { margin: 0; padding: 0; box-sizing: border-box; }
  html, body {
    width: 1200px; height: 871px; overflow: hidden;
    background: var(--bg);
    font-family: "Open Sans", Arial, sans-serif;
  }
  .stage { position: relative; width: 1200px; height: 871px; }

  .card {
    position: absolute; top: 287px;
    width: 520px; height: 297px;
    overflow: hidden;
    background: linear-gradient(135deg, var(--card) 0%, var(--card) 55%, var(--card-shade) 100%);
  }
  .card--back { left: 50px; }
  .card--front { left: 630px; }

  /* Diagonal watermark zone reserved for the brand symbol */
  .brand-mark-area { position: absolute; top: 0; bottom: 0; width: 250px; }
  .card--back .brand-mark-area {
    left: 0;
    clip-path: polygon(0 0, 100% 0, 55% 100%, 0 100%);
    background: linear-gradient(120deg, var(--mark-dark) 0%, var(--mark-mid) 55%, rgba(255,255,255,0) 100%);
  }
  .card--front .brand-mark-area {
    right: 0;
    clip-path: polygon(30% 0, 100% 0, 100% 100%, 0 100%);
    background: linear-gradient(300deg, var(--mark-dark) 0%, var(--mark-mid) 55%, rgba(255,255,255,0) 100%);
  }

  .brand { display: flex; align-items: center; gap: 8px; }
  .brand__square { width: 14px; height: 14px; background: var(--brand-blue); flex: none; }
  .brand__name {
    font-weight: 600; color: var(--brand-blue);
    font-size: 28px; letter-spacing: 1px; text-transform: uppercase; line-height: 1;
    white-space: nowrap;
  }
  .tagline {
    font-weight: 700; color: var(--ink); font-size: 13px; letter-spacing: 0.5px;
    margin-top: 4px; margin-left: 22px; white-space: nowrap;
  }

  .card--back .identity { position: absolute; left: 250px; top: 112px; }
  .card--back .website {
    position: absolute; left: 272px; top: 176px;
    font-size: 13px; color: var(--ink-soft);
  }

  .card--front .identity { position: absolute; left: 28px; top: 30px; }
  .card--front .brand__name { font-size: 26px; }

  .person { position: absolute; left: 28px; top: 108px; }
  .person__name { font-size: 18px; font-weight: 600; color: var(--brand-blue); }
  .person__role { font-size: 11px; color: var(--ink-soft); margin-top: 2px; }
  .address {
    position: absolute; left: 28px; top: 168px;
    font-size: 11px; color: var(--ink-soft); line-height: 1.5; font-style: normal;
  }
  .contacts {
    position: absolute; left: 28px; top: 212px; list-style: none;
    font-size: 11px; color: var(--ink-soft); line-height: 1.6;
  }
  .contacts li { display: flex; align-items: center; gap: 7px; }
  .contacts svg { width: 11px; height: 11px; fill: var(--brand-blue); }
</style>
</head>
<body>
<main class="stage">

  <section class="card card--back" aria-label="Card back">
    <div class="brand-mark-area" role="img" aria-label="Large diagonal brand symbol watermark in black and grey"></div>
    <div class="identity">
      <div class="brand">
        <span class="brand__square"></span>
        <span class="brand__name">qLM Builders</span>
      </div>
      <p class="tagline">Nimble Site Crafting</p>
    </div>
    <p class="website">www.qlmbuilders.com</p>
  </section>

  <section class="card card--front" aria-label="Card front">
    <div class="brand-mark-area" role="img" aria-label="Large diagonal brand symbol watermark in black and grey"></div>
    <div class="identity">
      <div class="brand">
        <span class="brand__square"></span>
        <span class="brand__name">qLM Builders</span>
      </div>
      <p class="tagline">Nimble Site Crafting</p>
    </div>
    <div class="person">
      <p class="person__name">Gavin Ostrand</p>
      <p class="person__role">Owner, CEO</p>
    </div>
    <address class="address">214 Birchfield Lane<br>Corvale, WI 53790</address>
    <ul class="contacts">
      <li>
        <svg viewBox="0 0 12 12" aria-hidden="true"><path d="M2.5 0.5 L4.5 0.5 L5.2 3.2 L3.9 4.3 C4.6 5.8 6.2 7.4 7.7 8.1 L8.8 6.8 L11.5 7.5 L11.5 9.5 C11.5 10.6 10.6 11.5 9.5 11.5 C4.5 11.2 0.8 7.5 0.5 2.5 C0.5 1.4 1.4 0.5 2.5 0.5 Z"/></svg>
        5550147823
      </li>
      <li>
        <svg viewBox="0 0 12 12" aria-hidden="true"><path d="M0.5 2 H11.5 V10 H0.5 Z M1.2 2.6 L6 6.5 L10.8 2.6" fill="none" stroke="#2aa6d9" stroke-width="1.2"/></svg>
        gavin@qlmbuilders.com
      </li>
      <li>
        <svg viewBox="0 0 12 12" aria-hidden="true"><circle cx="6" cy="6" r="5.3" fill="none" stroke="#2aa6d9" stroke-width="1.2"/><path d="M0.8 6 H11.2 M6 0.8 C3.5 3.5 3.5 8.5 6 11.2 M6 0.8 C8.5 3.5 8.5 8.5 6 11.2" fill="none" stroke="#2aa6d9" stroke-width="1"/></svg>
        www.qlmbuilders.com
      </li>
    </ul>
  </section>

</main>
</body>
</html>
```